Business cards Design for advertising technology Argentur

Hi guys,

we need a cool, simple business card design for our Company "Zentravio17".
It should be clean, but also special - it should be an eye catcher!

Our Logo is attached.
The format should be 85x55m.

The adress is:
Obere Kranzinger Str. 14.
9520 Kranzdorf
Tel: 04251 62914

```html
<!DOCTYPE html>
<html lang="en">
<head>
<meta charset="utf-8">
<title>Zentravio17 – Business Card</title>
<link href="https://fonts.googleapis.com/css2?family=Montserrat:wght@700;800&family=Open+Sans:wght@400;600;700&display=swap" rel="stylesheet">
<style>
  :root {
    --stage: #e9eaec;
    --card-white: #ffffff;
    --orange: #f39c12;
    --orange-deep: #ee8a0a;
    --orange-light: #f7b02a;
    --ink: #222222;
    --ink-soft: #3a3a3a;
    --tab-grey: #dcdcdc;
  }
  * { box-sizing: border-box; margin: 0; padding: 0; }
  html, body {
    width: 1200px; height: 807px; overflow: hidden;
    background: var(--stage);
    font-family: "Open Sans", Arial, sans-serif;
  }
  .stage { position: relative; width: 1200px; height: 807px; }

  .card {
    position: absolute; top: 248px;
    width: 480px; height: 310px;
    border-radius: 24px; overflow: hidden;
    box-shadow: 0 10px 28px rgba(0,0,0,.18);
  }
  .card--front { left: 90px; background: var(--card-white); }
  .card--back {
    left: 630px;
    background: linear-gradient(135deg, var(--orange-light), var(--orange-deep));
  }

  /* corner tabs */
  .tab { position: absolute; }
  .card--front .tab { background: var(--orange); }
  .card--front .tab--top { left: 0; top: 44px; width: 10px; height: 58px; border-radius: 0 6px 6px 0; }
  .card--front .tab--corner { right: 0; bottom: 0; width: 70px; height: 10px; border-radius: 6px 0 0 0; }
  .card--front .tab--side { right: 0; bottom: 0; width: 10px; height: 60px; border-radius: 6px 0 0 0; }
  .card--back .tab { background: var(--tab-grey); }
  .card--back .tab--top { left: 40px; top: 0; width: 64px; height: 8px; border-radius: 0 0 5px 5px; }
  .card--back .tab--side { right: 0; top: 210px; width: 8px; height: 64px; border-radius: 5px 0 0 5px; }

  /* front content */
  .brand {
    position: absolute; display: flex; align-items: center; gap: 10px;
    font-family: "Montserrat", Arial, sans-serif; font-weight: 800;
    letter-spacing: .5px; white-space: nowrap;
  }
  .card--front .brand { left: 112px; top: 58px; font-size: 34px; color: var(--ink); }
  .brand__mark { width: 30px; height: 30px; border-radius: 4px; background: var(--ink); flex: none; }

  .person { position: absolute; left: 60px; top: 140px; width: 160px; text-align: right; }
  .person__name { color: var(--orange); font-weight: 700; font-size: 17px; white-space: nowrap; }
  .person__role { color: var(--ink-soft); font-size: 10px; font-weight: 600; letter-spacing: .5px; margin-top: 2px; white-space: nowrap; }

  .divider { position: absolute; left: 238px; top: 140px; width: 2px; height: 66px; background: var(--orange); }

  .contacts { position: absolute; left: 254px; top: 138px; list-style: none; }
  .contacts li {
    display: flex; align-items: center; gap: 7px;
    font-size: 12.5px; color: var(--ink-soft); line-height: 22px; white-space: nowrap;
  }
  .contacts svg { width: 12px; height: 12px; fill: var(--orange); flex: none; }
  .contacts .web { color: var(--orange); }

  .address {
    position: absolute; left: 40px; bottom: 40px;
    font-size: 12.5px; color: var(--ink-soft); white-space: nowrap;
  }

  /* back content */
  .card--back .brand {
    left: 50%; top: 50%; transform: translate(-50%, -50%);
    flex-direction: column; gap: 14px;
    font-size: 36px; color: #ffffff;
  }
  .card--back .brand__mark {
    width: 76px; height: 76px; border-radius: 50%;
    background: transparent; border: 6px solid #ffffff;
  }
</style>
</head>
<body>
<main class="stage">

  <section class="card card--front" aria-label="Card front">
    <span class="tab tab--top"></span>
    <span class="tab tab--corner"></span>
    <span class="tab tab--side"></span>

    <div class="brand"><span class="brand__mark"></span>ZENTRAVIO17</div>

    <div class="person">
      <p class="person__name">Lena Hofbauer</p>
      <p class="person__role">OPERATION MANAGER</p>
    </div>

    <span class="divider"></span>

    <ul class="contacts">
      <li>
        <svg viewBox="0 0 24 24" aria-hidden="true"><path d="M6.6 10.8a15.1 15.1 0 0 0 6.6 6.6l2.2-2.2a1 1 0 0 1 1-.25 11.4 11.4 0 0 0 3.6.57 1 1 0 0 1 1 1V20a1 1 0 0 1-1 1A17 17 0 0 1 3 4a1 1 0 0 1 1-1h3.5a1 1 0 0 1 1 1c0 1.25.2 2.45.57 3.57a1 1 0 0 1-.25 1z"/></svg>
        04251 62914
      </li>
      <li>
        <svg viewBox="0 0 24 24" aria-hidden="true"><path d="M2 5h20v2l-10 7L2 7z M2 9l10 7 10-7v10H2z"/></svg>
        info@zentravio17.example
      </li>
      <li>
        <svg viewBox="0 0 24 24" aria-hidden="true"><circle cx="12" cy="12" r="10"/></svg>
        <span class="web">www.zentravio17.example</span>
      </li>
    </ul>

    <p class="address">Obere Kranzinger Str. 14. 9520 Kranzdorf</p>
  </section>

  <section class="card card--back" aria-label="Card back">
    <span class="tab tab--top"></span>
    <span class="tab tab--side"></span>
    <div class="brand"><span class="brand__mark"></span>ZENTRAVIO17</div>
  </section>

</main>
</body>
</html>
```